I want a business card that is going to show a creative spark but without limiting me to an industry. Something edgy but that wont go out of date. I want it state My business name Verity Lanes, profession - Professional Makeup Artist contact number and email

My service is to provide makeup services from bridal, fashion, photography, film, TV and so on. It is creative and different so i want that to be reflected.

I would like the card double sided.
Updates

 I would LOVE a background on my card something like this image... i can supply an image to be formed like this

Please use the image uploaded

Can we try using the image provided on one side of the card and then writing and details on the other side

Target Market(s)

I am targeting a wide range of people from Creative directors to the individual eg. bride

Industry/Entity Type

Business

Requirements
Must have
• Name: Harriet Cole
contact numbe 0417 583 940
email address:info@veritylanes.example
website: www.veritylanes.example
One of the images attached

professional makeup artist / hair stylist

I want it to show creativity
Nice to have
• logo, Double-sided card
Should not have
• the design should not use tradional style. Or images that are not my own

```html
<!DOCTYPE html>
<html lang="en">
<head>
<meta charset="utf-8">
<title>Verity Lanes – Professional Makeup Artist</title>
<link rel="stylesheet" href="https://fonts.googleapis.com/css2?family=Pinyon+Script&family=Federo&family=Stint+Ultra+Condensed&display=swap">
<style>
  :root {
    --teal: #4f9bb0;
    --tan: #dcaa72;
    --ink: #111111;
    --card-w: 722px;
    --card-h: 1200px;
  }
  * { margin: 0; padding: 0; box-sizing: border-box; }
  html, body {
    width: var(--card-w);
    height: var(--card-h);
    overflow: hidden;
    background: var(--tan);
  }
  .card {
    position: relative;
    width: var(--card-w);
    height: var(--card-h);
    overflow: hidden;
    color: var(--ink);
  }
  .card__marble {
    position: absolute;
    inset: 0;
    width: 100%;
    height: 100%;
  }
  .brand-name {
    position: absolute;
    top: 0;
    left: 0;
    width: 100%;
    height: 360px;
    font-family: "Pinyon Script", cursive;
    font-weight: 400;
    line-height: 1;
  }
  .brand-name__first,
  .brand-name__last {
    position: absolute;
    font-size: 122px;
    white-space: nowrap;
  }
  .brand-name__first { left: 30px; top: 40px; }
  .brand-name__last { left: 330px; top: 190px; }
  .profession {
    position: absolute;
    top: 508px;
    left: 0;
    width: 100%;
    text-align: center;
    font-family: "Federo", sans-serif;
    line-height: 1.05;
  }
  .profession__title { display: block; font-size: 74px; }
  .profession__role { display: block; font-size: 58px; }
  .contact {
    position: absolute;
    top: 1030px;
    left: 0;
    width: 100%;
    text-align: center;
    line-height: 1.05;
  }
  .contact__phone {
    display: block;
    font-family: "Federo", sans-serif;
    font-size: 58px;
    letter-spacing: 2px;
  }
  .contact__email {
    display: block;
    font-family: "Stint Ultra Condensed", sans-serif;
    font-size: 90px;
    letter-spacing: 1px;
    white-space: nowrap;
  }
</style>
</head>
<body>
  <main class="card">
    <svg class="card__marble" role="img" aria-label="Marbled swirl pattern in teal and tan" viewBox="0 0 722 1200" preserveAspectRatio="none">
      <defs>
        <linearGradient id="marble-tone" x1="0" y1="0" x2="1" y2="1">
          <stop offset="0" stop-color="#4f9bb0"/>
          <stop offset="0.45" stop-color="#6fa3a8"/>
          <stop offset="0.75" stop-color="#c9a77d"/>
          <stop offset="1" stop-color="#dcaa72"/>
        </linearGradient>
      </defs>
      <rect width="722" height="1200" fill="url(#marble-tone)"/>
    </svg>

    <h1 class="brand-name">
      <span class="brand-name__first">Verity</span>
      <span class="brand-name__last">Lanes</span>
    </h1>

    <p class="profession">
      <span class="profession__title">Professional</span>
      <span class="profession__role">Makeup Artist</span>
    </p>

    <p class="contact">
      <span class="contact__phone">0417 583 940</span>
      <span class="contact__email">info@veritylanes.example</span>
    </p>
  </main>
</body>
</html>
```